4th Generation Family Business Needs a New Card Design!

We are a family owned 4th Generation company. We are based in the Sydney, Australia area and we are desperately in need of a more modern and classy card. We are monumental masons who design, supply & erect lasting memorials throughout cemeteries in Sydney. Our customers are normally in a period of grieving. I have attached logo files that will need to be implemented on the card. Company was established 1935. Australian Owned and Operated. Card needs to be designed to PRINTLY.com specification.

Target Market(s)

Our target market is based upon people that a grieving for family members that have passed away. We also deal with alot of companies that own and operate cemeteries.

Industry/Entity Type

Business

Contact Information for Business Card

Oliver Brantley, Operations Manager, 0417552908, oliver@hollowaystoneworks.com.au
Martin Brantley, Director, 0431906627, martin@hollowaystoneworks.com.au
Phone # 02 9634 2258
Website: www.hollowaystoneworks.com.au
Address: Suite 17, 8 Calloway Lane, East Penrose, Sydney NSW 2290

Font styles to use
Serif
Decorative
Script

Requirements
Must have
• Would like to see the logo nicely implemented with a modern design. Embossed lettering would be a nice additive.

```html
<!DOCTYPE html>
<html lang="en">
<head>
<meta charset="utf-8">
<title>Holloway Stoneworks – Business Card</title>
<link rel="stylesheet" href="https://fonts.googleapis.com/css2?family=Cinzel:wght@400&family=Roboto:wght@400;500&display=swap">
<style>
  :root {
    --backdrop: #ececec;
    --card-white: #fbfbfb;
    --card-black: #1c1c1c;
    --gold: #e2b53a;
    --charcoal: #2a2a2a;
    --text-grey: #6b6b6b;
    --rule-grey: #d9d9d9;
    --back-text: #ffffff;
  }
  * { margin: 0; padding: 0; box-sizing: border-box; }
  html, body { width: 1200px; height: 960px; overflow: hidden; }
  body {
    background: var(--backdrop);
    position: relative;
    font-family: "Roboto", Arial, sans-serif;
  }
  .card {
    position: absolute;
    top: 332px;
    width: 520px;
    height: 297px;
    border-radius: 3px;
    box-shadow: 0 10px 28px rgba(0,0,0,0.12);
  }
  .card--front { left: 60px; background: var(--card-white); }
  .card--back { left: 620px; background: var(--card-black); }

  /* front */
  .brand-block {
    position: absolute;
    left: 28px; top: 0; bottom: 0;
    width: 186px;
    display: flex;
    align-items: center;
    gap: 12px;
  }
  .brand-square {
    width: 64px; height: 64px;
    background: var(--charcoal);
    flex: none;
  }
  .brand-name {
    font-family: "Roboto", Arial, sans-serif;
    font-weight: 500;
    font-size: 17px;
    line-height: 1.3;
    color: var(--charcoal);
  }
  .divider {
    position: absolute;
    left: 224px; top: 78px;
    width: 1px; height: 140px;
    background: var(--rule-grey);
  }
  .contact {
    position: absolute;
    left: 242px; top: 80px;
    color: var(--text-grey);
    font-size: 12.5px;
    line-height: 1.45;
  }
  .contact__name {
    font-family: "Cinzel", Georgia, serif;
    font-size: 19px;
    color: var(--gold);
    letter-spacing: 0.5px;
    line-height: 1.2;
  }
  .contact__role { font-size: 12px; margin-bottom: 6px; }
  .contact__address { margin-bottom: 4px; }
  .contact__line { display: flex; align-items: center; gap: 7px; }
  .contact__line svg { width: 10px; height: 10px; flex: none; fill: var(--gold); }

  /* back */
  .back-brand {
    position: absolute;
    inset: 0;
    display: flex;
    align-items: center;
    justify-content: center;
  }
  .back-brand__name {
    font-family: "Roboto", Arial, sans-serif;
    font-weight: 500;
    font-size: 30px;
    letter-spacing: 1px;
    color: var(--back-text);
  }
</style>
</head>
<body>

  <section class="card card--front" aria-label="Card front">
    <div class="brand-block">
      <span class="brand-square"></span>
      <span class="brand-name">Holloway<br>Stoneworks</span>
    </div>
    <div class="divider"></div>
    <div class="contact">
      <p class="contact__name">Oliver Brantley</p>
      <p class="contact__role">Operations Manager</p>
      <p class="contact__address">Suite 17, 8 Calloway Lane, East Penrose,<br>Sydney NSW 2290</p>
      <p class="contact__line">
        <svg viewBox="0 0 10 10"><rect x="2" y="0" width="6" height="10" rx="1"/></svg>0417552908
      </p>
      <p class="contact__line">
        <svg viewBox="0 0 10 10"><path d="M2 0 L4 2.5 L3 4 Q4.5 6 6 7 L7.5 6 L10 8 L8.5 10 Q3 9 0 1.5 Z"/></svg>02 9634 2258
      </p>
      <p class="contact__line">
        <svg viewBox="0 0 10 10"><rect x="0" y="2" width="10" height="6.5" rx="1"/></svg>oliver@hollowaystoneworks.com.au
      </p>
      <p class="contact__line">
        <svg viewBox="0 0 10 10"><circle cx="5" cy="5" r="5"/></svg>www.hollowaystoneworks.com.au
      </p>
    </div>
  </section>

  <section class="card card--back" aria-label="Card back">
    <div class="back-brand">
      <p class="back-brand__name">Holloway Stoneworks</p>
    </div>
  </section>

</body>
</html>
```